Fresh Business Card Designs Required

Looking to get new business cards but want a fresh look and feel. The logo has a large curved square which can be incorporated, or alternative the text-only version of the logo can be utilised if it is better. Looking for fresh ideas. I prefer flat designs, also incorporating a QR code to our contact us page on website would be great to make contact easy.
Updates

I have just uploaded the .ai files for our logo to make it easier to drop into your designs. Thanks for your consideration looking forward to seeing the results!

Target Market(s)

Generally business cards are handed to consumers who are contacting us for information.

Industry/Entity Type

Water Pumping and Irrigation, Water Filtration,

Contact Information for Business Card

Company Name / Logo, Name, Job Title, Phone No., Direct Line, Address

Font styles to use
Sans Serif

Colors
00AB8E
00BBA5
67D7C9
C6EFE9
E9F9F6
FFF300
FFF600
FEFA6F
FFFEC7
FFFEE8

Requirements
Must have
• Contact Details!!!! :)
Nice to have
• QR Code to contact us page, list of products (not critical!)

```html
<!DOCTYPE html>
<html lang="en">
<head>
<meta charset="utf-8">
<title>South Ridge Power &amp; Water – Business Card</title>
<link href="https://fonts.googleapis.com/css2?family=Montserrat:wght@400;500;700;800&display=swap" rel="stylesheet">
<style>
  :root {
    --brand-green: #43b649;
    --brand-yellow: #f2e20a;
    --paper: #ffffff;
    --ink: #222222;
    --backdrop: #e9ebe8;
  }
  * { box-sizing: border-box; margin: 0; padding: 0; }
  html, body { width: 1200px; height: 912px; overflow: hidden; }
  body {
    background: var(--backdrop);
    font-family: "Montserrat", Arial, sans-serif;
    position: relative;
  }
  .card {
    position: absolute;
    width: 560px;
    height: 320px;
    border-radius: 4px;
    overflow: hidden;
    box-shadow: 0 10px 24px rgba(0,0,0,.18);
  }

  /* Shared name mark: one colour, one weight, plain square beside */
  .name-mark {
    position: absolute;
    display: flex; align-items: center; gap: 12px;
    font-weight: 700; white-space: nowrap;
  }
  .name-mark .mark-square {
    flex: none; background: var(--brand-yellow); border-radius: 3px;
  }

  /* Front */
  .card-front { left: 60px; top: 70px; background: var(--brand-green); color: var(--paper); }
  .card-front .name-mark {
    left: 0; right: 0; top: 136px; justify-content: center;
    font-size: 30px; color: var(--paper);
  }
  .card-front .mark-square { width: 30px; height: 30px; }
  .front-url {
    position: absolute; right: 60px; bottom: 40px;
    font-size: 13px; letter-spacing: 3px; font-weight: 400;
  }
  .front-url .accent { color: var(--brand-yellow); }

  /* Back */
  .card-back { left: 580px; top: 520px; background: var(--paper); color: var(--ink); }
  .back-tab {
    position: absolute; left: -10px; top: 60px;
    width: 24px; height: 34px; border-radius: 6px;
    background: var(--brand-yellow);
  }
  .card-back .name-mark {
    right: 28px; top: 26px; font-size: 15px; color: var(--brand-green); gap: 8px;
  }
  .card-back .mark-square { width: 14px; height: 14px; border-radius: 2px; }

  .contact { position: absolute; left: 34px; top: 56px; }
  .contact-name {
    color: var(--brand-green); font-weight: 800; font-size: 20px;
    text-transform: uppercase; letter-spacing: .5px; line-height: 1.1;
  }
  .contact-role { font-size: 13px; font-weight: 500; margin: 2px 0 10px; }
  .contact-row { display: flex; align-items: center; gap: 6px; font-size: 13px; line-height: 1.45; }
  .contact-row svg { width: 10px; height: 10px; flex: none; }
  .contact-row .accent { color: var(--brand-green); }
  .contact-address { font-size: 13px; margin-top: 8px; line-height: 1.35; }

  .service-band {
    position: absolute; left: 0; right: 0; bottom: 0; height: 124px;
    background: var(--brand-green); color: var(--paper);
    border-top: 4px solid var(--brand-yellow);
  }
  .service-headline {
    display: flex; justify-content: flex-end; gap: 14px;
    padding: 8px 32px 6px 0;
    font-weight: 800; font-size: 17px; text-transform: uppercase;
  }
  .service-headline .divider { color: var(--brand-yellow); font-weight: 400; }
  .service-rule { height: 1px; margin-left: 60px; background: var(--brand-yellow); }
  .product-list {
    list-style: none; display: flex; flex-wrap: wrap;
    gap: 2px 12px; padding: 9px 28px 0 34px; font-size: 13.5px;
  }
  .product-list li { display: flex; align-items: center; gap: 6px; }
  .product-list li::before {
    content: ""; width: 6px; height: 6px; border-radius: 50%;
    background: var(--brand-yellow);
  }
</style>
</head>
<body>

<section class="card card-front" aria-label="Business card front">
  <div class="name-mark"><span class="mark-square"></span>South Ridge Power &amp; Water</div>
  <div class="front-url">www.<span class="accent">srpw</span>.com</div>
</section>

<section class="card card-back" aria-label="Business card back">
  <div class="back-tab"></div>

  <div class="name-mark"><span class="mark-square"></span>South Ridge Power &amp; Water</div>

  <div class="contact">
    <div class="contact-name">Marcus Delane</div>
    <div class="contact-role">Managing Director</div>
    <div class="contact-row">
      <svg viewBox="0 0 10 10"><path d="M2 0.5 L3.6 2.6 L2.8 3.6 Q4 6 6.4 7.2 L7.4 6.4 L9.5 8 L8.4 9.5 Q3 9 0.5 1.6 Z" fill="var(--brand-green)"/></svg>
      +6650 1287
    </div>
    <div class="contact-row">
      <svg viewBox="0 0 10 10"><circle cx="5" cy="5" r="4.4" fill="none" stroke="var(--brand-green)" stroke-width="1.1"/><path d="M0.6 5 H9.4 M5 0.6 Q2 5 5 9.4 M5 0.6 Q8 5 5 9.4" fill="none" stroke="var(--brand-green)" stroke-width="0.8"/></svg>
      <span>www.<span class="accent">srpw</span>.com</span>
    </div>
    <div class="contact-address">27 Harlow Close,<br>Bayview NSW 2471</div>
  </div>

  <div class="service-band">
    <div class="service-headline">
      <span>Sales</span><span class="divider">|</span>
      <span>Service</span><span class="divider">|</span>
      <span>Repairs</span>
    </div>
    <div class="service-rule"></div>
    <ul class="product-list">
      <li>Solar Power Systems</li>
      <li>Hot Water Systems</li>
      <li>Energy Storage</li>
      <li>Solar Pumping</li>
      <li>Generators</li>
      <li>Irrigation</li>
      <li>Filtration</li>
      <li>Pumps</li>
      <li>Tanks</li>
    </ul>
  </div>
</section>

</body>
</html>
```